out of the box Business Card Design for a Manufacturer / Distributor

We are a manufarturer and distributor of products.
the company name is VORTANI (Pic attached)

the picture is NOT a must have on the business Card.

the Business Card should look really professional and/or special, so out of the box thinking is welcome.

there should be 2 Adresses on the Business Card for Main and Branch Office.
Email Adress, homepage, Name is required
NO Phone Number

Our working field:
Private Labeling
high Quality Production
direct distribution
warehousing
trademark registration
legal support

Main Office:
Kornblumenweg 14
08352 Burgstädt
Germany

Branch Office:
Daska Lane
Sialkot
Pakistan

Names:
Lukas Feldhaus (Owner)
Imran Qureshi (Owner)

Email:
lukas@vortani-example.com
imran@vortani-example.com

homepage:
vortani-example.com

Industry/Entity Type

Manufacturer Distributer

Contact Information for Business Card

Vortani

Requirements
Must have
• Names, both office Adresses, email, homepage
Should not have
• Phone Number

```html
<!DOCTYPE html>
<html lang="en">
<head>
<meta charset="utf-8">
<title>Vortani Business Card</title>
<link rel="stylesheet" href="https://fonts.googleapis.com/css2?family=Poppins:wght@400;500;600&display=swap">
<style>
  :root {
    --page-bg: #eeeeee;
    --card-dark: #161616;
    --card-mid: #262626;
    --ink-light: #ffffff;
    --ink-soft: #cfcfcf;
    --accent-orange: #e8642c;
    --accent-magenta: #b23a6e;
    --accent-purple: #7b2fb3;
  }
  * { box-sizing: border-box; margin: 0; padding: 0; }
  html, body { width: 1200px; height: 2524px; overflow: hidden; }
  body {
    background: var(--page-bg);
    font-family: "Poppins", sans-serif;
    color: var(--ink-light);
    position: relative;
  }
  .card {
    position: absolute;
    left: 60px;
    width: 1080px;
    height: 620px;
    background: linear-gradient(135deg, var(--card-mid), var(--card-dark) 70%);
    overflow: hidden;
    box-shadow: 0 10px 30px rgba(0,0,0,.18);
  }
  .card-front { top: 560px; }
  .card-back { top: 1300px; }

  .front-artwork {
    position: absolute;
    right: 0; top: 0;
    width: 440px; height: 620px;
    background:
      radial-gradient(ellipse 70% 60% at 70% 40%,
        rgba(232,100,44,.55), rgba(178,58,110,.4) 45%, rgba(123,47,179,.25) 70%, rgba(22,22,22,0) 100%);
  }
  .front-accent-band {
    position: absolute;
    left: 0; bottom: 70px;
    width: 100%; height: 40px;
    background: linear-gradient(90deg, rgba(232,100,44,0), rgba(232,100,44,.18) 30%, rgba(123,47,179,.22) 80%, rgba(123,47,179,0));
  }

  .brand { position: absolute; display: flex; align-items: center; gap: 18px; }
  .brand-dot { border-radius: 50%; background: var(--ink-light); }
  .brand-name { font-weight: 500; letter-spacing: 2px; color: var(--ink-light); }
  .card-front .brand { left: 70px; top: 262px; }
  .card-front .brand-dot { width: 62px; height: 62px; }
  .card-front .brand-name { font-size: 64px; }
  .card-back .brand { left: 70px; top: 62px; gap: 14px; }
  .card-back .brand-dot { width: 40px; height: 40px; }
  .card-back .brand-name { font-size: 40px; }

  .working-field { position: absolute; left: 70px; top: 200px; }
  .section-title {
    color: var(--accent-orange);
    font-weight: 600;
    font-size: 26px;
    letter-spacing: 1px;
    margin-bottom: 20px;
  }
  .field-list { list-style: none; }
  .field-list li {
    font-size: 21px;
    color: var(--ink-soft);
    line-height: 44px;
    display: flex;
    align-items: center;
    gap: 22px;
  }
  .field-list li::before {
    content: "";
    width: 10px; height: 10px;
    background: var(--accent-orange);
  }

  .contacts { position: absolute; left: 590px; top: 64px; width: 450px; }
  .person { margin-bottom: 22px; }
  .person-name { font-size: 36px; font-weight: 500; line-height: 1.15; }
  .person-role {
    font-size: 15px; letter-spacing: 6px; color: var(--accent-orange);
    font-weight: 500; margin: 4px 0 6px;
  }
  .contact-line { display: flex; align-items: center; gap: 12px; font-size: 19px; color: var(--ink-soft); }
  .contact-line svg { flex: none; }

  .offices { display: flex; gap: 60px; margin-top: 6px; }
  .office-title { color: var(--accent-orange); font-weight: 600; font-size: 17px; letter-spacing: 1px; margin-bottom: 8px; }
  .office-body { display: flex; gap: 10px; font-size: 15px; line-height: 22px; color: var(--ink-soft); }
  .office-body svg { flex: none; margin-top: 2px; }
  .website { margin-top: 26px; }
</style>
</head>
<body>

<section class="card card-front" aria-label="Card front">
  <div class="front-artwork" role="img" aria-label="Decorative orange to purple gradient artwork"></div>
  <div class="front-accent-band" role="img" aria-label="Decorative gradient accent line"></div>
  <div class="brand">
    <span class="brand-dot"></span>
    <span class="brand-name">VORTANI</span>
  </div>
</section>

<section class="card card-back" aria-label="Card back">
  <div class="brand">
    <span class="brand-dot"></span>
    <span class="brand-name">VORTANI</span>
  </div>

  <div class="working-field">
    <h2 class="section-title">OUR WORKING FIELD</h2>
    <ul class="field-list">
      <li>Private Labeling</li>
      <li>High Quality Production</li>
      <li>Direct distribution</li>
      <li>Warehousing</li>
      <li>Trademark registration</li>
      <li>Legal support</li>
    </ul>
  </div>

  <div class="contacts">
    <div class="person">
      <p class="person-name">Lukas Feldhaus</p>
      <p class="person-role">OWNER</p>
      <p class="contact-line">
        <svg width="22" height="16" viewBox="0 0 22 16"><rect x="1" y="1" width="20" height="14" fill="none" stroke="#e8642c" stroke-width="2"/><path d="M1 1 L11 9 L21 1" fill="none" stroke="#e8642c" stroke-width="2"/></svg>
        lukas@vortani-example.com
      </p>
    </div>
    <div class="person">
      <p class="person-name">Imran Qureshi</p>
      <p class="person-role">OWNER</p>
      <p class="contact-line">
        <svg width="22" height="16" viewBox="0 0 22 16"><rect x="1" y="1" width="20" height="14" fill="none" stroke="#e8642c" stroke-width="2"/><path d="M1 1 L11 9 L21 1" fill="none" stroke="#e8642c" stroke-width="2"/></svg>
        imran@vortani-example.com
      </p>
    </div>

    <div class="offices">
      <div class="office">
        <p class="office-title">MAIN OFFICE</p>
        <div class="office-body">
          <svg width="16" height="22" viewBox="0 0 16 22"><path d="M8 1 C4 1 1 4 1 8 C1 13 8 21 8 21 C8 21 15 13 15 8 C15 4 12 1 8 1 Z" fill="#e8642c"/><circle cx="8" cy="8" r="3" fill="#161616"/></svg>
          <p>Kornblumenweg 14<br>08352 Burgstädt<br>Germany</p>
        </div>
      </div>
      <div class="office">
        <p class="office-title">BRANCH OFFICE</p>
        <div class="office-body">
          <svg width="16" height="22" viewBox="0 0 16 22"><path d="M8 1 C4 1 1 4 1 8 C1 13 8 21 8 21 C8 21 15 13 15 8 C15 4 12 1 8 1 Z" fill="#e8642c"/><circle cx="8" cy="8" r="3" fill="#161616"/></svg>
          <p>Daska Lane<br>Sialkot<br>Pakistan</p>
        </div>
      </div>
    </div>

    <p class="contact-line website">
      <svg width="20" height="20" viewBox="0 0 20 20"><circle cx="10" cy="10" r="8.5" fill="none" stroke="#e8642c" stroke-width="2"/><ellipse cx="10" cy="10" rx="4" ry="8.5" fill="none" stroke="#e8642c" stroke-width="1.6"/><path d="M1.5 10 H18.5" stroke="#e8642c" stroke-width="1.6"/></svg>
      vortani-example.com
    </p>
  </div>
</section>

</body>
</html>
```